Venture Capital Firm needs new Business Cards

We need a business card design for "Stonebrook Partners". We already have a logo which we are happy with - we now need to have business cards designed.
Stonebrook is a venture capital firm, which means that we look to invest in technology start-ups. See our website www.stonebrookpx.example for more details.
Updates
Project Deadline Extended Reason: Apologies for not being very responsive. Will push back the deadline a couple days in order to give feedback and allow other people to present designs. Added Wednesday, October 22, 2014
Industry/Entity Type
Business
Look and feel
Each slider illustrates characteristics of the customer's brand and the style your logo design should communicate.

```html
<!DOCTYPE html>
<html lang="en">
<head>
<meta charset="utf-8">
<title>Stonebrook Partners – Business Cards</title>
<link href="https://fonts.googleapis.com/css2?family=Lato:wght@400;700&family=Montserrat:wght@700&display=swap" rel="stylesheet">
<style>
  :root {
    --backdrop: #e6e4e1;
    --card: #ffffff;
    --brand-blue: #34499b;
    --charcoal: #464547;
    --bar-grey: #dcdcdc;
    --ink: #333333;
    --magenta: #b9528f;
    --pink: #e6648b;
    --orange: #e58b56;
    --yellow: #e7b94a;
  }
  html, body {
    margin: 0;
    padding: 0;
    width: 900px;
    height: 1200px;
    overflow: hidden;
    background: var(--backdrop);
  }
  .canvas {
    position: relative;
    width: 900px;
    height: 1200px;
  }
  .card {
    position: absolute;
    left: 80px;
    width: 740px;
    height: 470px;
    background: var(--card);
    box-shadow: 0 10px 24px rgba(0,0,0,0.18);
    overflow: hidden;
  }
  .card--front { top: 90px; }
  .card--back { top: 640px; }

  .card__art {
    position: absolute;
    inset: 0;
    width: 740px;
    height: 470px;
  }
  .company {
    position: absolute;
    left: 30px;
    top: 130px;
    margin: 0;
    font-family: "Montserrat", sans-serif;
    font-weight: 700;
    font-size: 27px;
    letter-spacing: 0.2px;
    color: var(--brand-blue);
  }
  .address {
    position: absolute;
    left: 30px;
    top: 167px;
    margin: 0;
    font-family: "Lato", sans-serif;
    font-size: 15px;
    color: var(--ink);
  }
  .person {
    position: absolute;
    left: 30px;
    top: 345px;
    width: 200px;
    text-align: center;
    color: #fff;
  }
  .person__name {
    margin: 0;
    font-family: "Montserrat", sans-serif;
    font-weight: 700;
    font-size: 24px;
  }
  .person__role {
    margin: 0;
    font-family: "Lato", sans-serif;
    font-size: 15px;
  }
  .contact {
    position: absolute;
    right: 110px;
    margin: 0;
    font-family: "Lato", sans-serif;
    font-size: 13.5px;
    line-height: 19px;
    text-align: right;
    color: var(--ink);
  }
  .contact--web { top: 301px; }
  .contact--phone { top: 364px; }

  .wordmark {
    position: absolute;
    left: 0;
    right: 0;
    top: 175px;
    display: flex;
    align-items: center;
    justify-content: center;
    gap: 16px;
  }
  .wordmark__dot {
    width: 30px;
    height: 30px;
    border-radius: 50%;
    background: var(--brand-blue);
  }
  .wordmark__name {
    font-family: "Lato", sans-serif;
    font-weight: 700;
    font-size: 46px;
    color: var(--brand-blue);
  }
</style>
</head>
<body>
<main class="canvas">

  <section class="card card--front" aria-label="Business card front">
    <svg class="card__art" viewBox="0 0 740 470" aria-hidden="true">
      <rect class="bar bar--web" x="250" y="295" width="490" height="53" fill="var(--bar-grey)"/>
      <rect class="bar bar--phone" x="250" y="357" width="490" height="54" fill="var(--bar-grey)"/>
      <polygon class="name-panel" points="0,295 262,295 382,470 0,470" fill="var(--charcoal)"/>
      <polygon points="344,416 434,416 472,470 382,470" fill="var(--magenta)"/>
      <polygon points="434,416 524,416 562,470 472,470" fill="var(--pink)"/>
      <polygon points="524,416 614,416 652,470 562,470" fill="var(--orange)"/>
      <polygon points="614,416 740,416 740,470 652,470" fill="var(--yellow)"/>
      <g class="icon icon--monitor" fill="var(--ink)">
        <rect x="648" y="304" width="38" height="27" rx="2"/>
        <rect x="652" y="308" width="30" height="19" fill="var(--bar-grey)"/>
        <rect x="664" y="331" width="6" height="5"/>
        <rect x="657" y="336" width="20" height="3"/>
      </g>
      <g class="icon icon--phone" fill="var(--ink)">
        <path d="M648 373 q19 -8 38 0 v7 h-9 v-4 q-10 -3 -20 0 v4 h-9 z"/>
        <path d="M656 380 h22 l6 16 h-34 z"/>
        <g fill="var(--bar-grey)">
          <rect x="661" y="384" width="3" height="2"/><rect x="666" y="384" width="3" height="2"/><rect x="671" y="384" width="3" height="2"/>
          <rect x="660" y="388" width="3" height="2"/><rect x="666" y="388" width="3" height="2"/><rect x="672" y="388" width="3" height="2"/>
        </g>
      </g>
    </svg>
    <h1 class="company">STONEBROOK PARTNERS</h1>
    <p class="address">48 Harbor Lane, Westfield 60418</p>
    <div class="person">
      <p class="person__name">DANIEL REYES</p>
      <p class="person__role">Manager</p>
    </div>
    <p class="contact contact--web">admin@stonebrookpartners.example<br>stonebrookpartners.example</p>
    <p class="contact contact--phone">000 - 4821 - 3907<br>000 - 6150 - 2748</p>
  </section>

  <section class="card card--back" aria-label="Business card back">
    <svg class="card__art" viewBox="0 0 740 470" aria-hidden="true">
      <rect class="base-band" x="0" y="417" width="740" height="53" fill="var(--charcoal)"/>
      <polygon points="400,417 488,417 526,470 438,470" fill="var(--magenta)"/>
      <polygon points="488,417 578,417 616,470 526,470" fill="var(--pink)"/>
      <polygon points="578,417 668,417 706,470 616,470" fill="var(--orange)"/>
      <polygon points="668,417 740,417 740,470 706,470" fill="var(--yellow)"/>
    </svg>
    <div class="wordmark">
      <span class="wordmark__dot"></span>
      <span class="wordmark__name">Stonebrook Partners</span>
    </div>
  </section>

</main>
</body>
</html>
```